Brackenfold Latches Business Cards

Need high quality business card designed around my company logo. Ideally the cards need to be a glossy black as the logo goes well with a black background.

The company is a Locksmithing business.

Domestic clients are Residential Home Owners and Landlords. Commercial clients are local businesses, estate agents, landlords, solicitors

Services offered :
Emergency Lock Out
New Lock Fitting & Replacement
High Security Upgrades
UPVC lock repairs
Mobile Key Cutting
Free Security Reviews

Qualificatons & Certifications:
Accredited Guild & Tower KSR Level 3, QTRB
Fully Insured
PVX Checked

Contact & Business Details:

Business Name : Brackenfold Latches
Name: Rob Fenwick
Tel: 01823 574419 Office / 07841592637 Mobile
Email: contact@brackenfoldlatches.com
Website: www.brackenfoldlatches.com

(please note that the website is currently under development and not available to view)

Locksmith

Name: Rob Fenwick

Services:
Emergency Lock Out
High Security Upgrades
UPVC lock repairs
Mobile Key Cutting
Free Security Reviews

• Ideally the cards should be a glossy black as the logo stands out better on a black background.

Logo on front and the word LOCKSMITH should be incorporated into the front design of the card.

Qualifications & Certifications on the back ideally along the top / bottom of the card or split (I.e along the top “ Accredited : Guild & Tower Level 3 , QTRB”
and along the bottom , “Fully Insured & PVX Checked”

Services offered ideally listed on the back of the card, preferably split into two columns. If possible the logo could also be incorporated onto the back of the card between the two services columns (I.e the services listed either side of the logo)
• On the back of the card, have the logo in the middle with the services listed either side of the logo I.e 3 services on left of logo and three to the right.

```html
<!DOCTYPE html>
<html lang="en">
<head>
<meta charset="utf-8">
<title>Brackenfold Latches Business Cards</title>
<link rel="stylesheet" href="https://fonts.googleapis.com/css2?family=Michroma&family=Quicksand:wght@500;600&display=swap">
<style>
  :root {
    --page: #ffffff;
    --card: #000000;
    --gold: #c8962e;
    --gold-soft: #b9872a;
    --bronze: #7f4614;
    --dash: #8a4f1b;
    --ink: #ffffff;
    --ink-dark: #1a1a1a;
  }
  * { margin: 0; padding: 0; box-sizing: border-box; }
  html, body {
    width: 1200px; height: 1200px; overflow: hidden;
    background: var(--page);
  }
  .sheet { position: relative; width: 1200px; height: 1200px; }
  .card {
    position: absolute; width: 775px; height: 431px;
    background: var(--card); overflow: hidden;
    font-family: "Quicksand", sans-serif; color: var(--ink);
  }
  .card--back { left: 215px; top: 156px; }
  .card--front { left: 217px; top: 621px; }

  .display {
    font-family: "Michroma", sans-serif;
    color: var(--gold); white-space: nowrap;
  }
  .rule { position: absolute; height: 2px; background: var(--gold); }
  .rule--bronze { background: var(--dash); }

  .accreditation {
    position: absolute; left: 0; right: 0; top: 34px;
    text-align: center; font-size: 17px; font-weight: 400;
  }
  .services-title {
    position: absolute; left: 0; right: 0; top: 88px;
    text-align: center; font-size: 15px; letter-spacing: 2.5px;
    color: var(--ink); white-space: nowrap;
  }
  .services-title .stars { color: var(--gold); letter-spacing: 4px; font-size: 13px; padding: 0 10px; }

  .service-list { position: absolute; list-style: none; font-size: 19px; font-weight: 500; line-height: 26px; }
  .service-list li { position: relative; padding-left: 0; }
  .service-list li::before {
    content: ""; position: absolute; left: -21px; top: 13px;
    width: 11px; height: 3px; background: var(--dash);
  }
  .service-list--left { left: 56px; top: 171px; }
  .service-list--left li:nth-child(1) { margin-bottom: 9px; }
  .service-list--left li:nth-child(2) { margin-bottom: 6px; }
  .service-list--right { left: 534px; top: 171px; }
  .service-list--right li { margin-bottom: 20px; }

  .brand-mark {
    position: absolute; border: 3px solid var(--gold); border-radius: 50%;
    display: flex; align-items: center; justify-content: center; text-align: center;
  }
  .brand-mark__name {
    font-family: "Quicksand", sans-serif; font-weight: 600; color: var(--gold);
    line-height: 1.15;
  }
  .card--back .brand-mark { left: 293px; top: 143px; width: 188px; height: 188px; }
  .card--back .brand-mark__name { font-size: 22px; }

  .assurance {
    position: absolute; left: 0; right: 0; top: 369px;
    text-align: center; font-size: 17px;
  }

  /* front */
  .tab-block { position: absolute; left: 0; top: 51px; width: 44px; height: 76px; background: var(--bronze); }
  .name-plate { position: absolute; left: 54px; top: 51px; width: 309px; height: 76px; background: var(--bronze); }
  .name-plate__name {
    position: absolute; left: 15px; top: 13px;
    font-family: "Michroma", sans-serif; font-size: 22px; color: var(--ink);
    letter-spacing: 0.5px; white-space: nowrap;
  }
  .name-plate__role {
    position: absolute; left: 15px; top: 41px;
    font-family: "Michroma", sans-serif; font-size: 11px; color: var(--ink); letter-spacing: 1px;
  }
  .name-plate__line {
    position: absolute; left: 15px; top: 63px; width: 255px; height: 2px;
    background: linear-gradient(90deg, var(--ink), rgba(255,255,255,0.2));
  }

  .contact { position: absolute; left: 69px; width: 340px; height: 52px; }
  .contact--phone { top: 177px; }
  .contact--web { top: 244px; }
  .contact--place { top: 311px; }
  .contact__icon {
    position: absolute; left: 0; top: 0; width: 52px; height: 52px;
    background: var(--bronze); border-radius: 0 14px 0 14px;
    display: flex; align-items: center; justify-content: center;
  }
  .contact__text {
    position: absolute; left: 68px; top: -1px;
    font-size: 17px; font-weight: 500; line-height: 26.5px; white-space: nowrap;
  }

  .card--front .brand-mark { left: 527px; top: 129px; width: 152px; height: 152px; }
  .card--front .brand-mark__name { font-size: 18px; }
  .trade {
    position: absolute; left: 453px; width: 300px; top: 290px;
    text-align: center; font-size: 23px; letter-spacing: 1px;
  }

  .footer-band { position: absolute; left: 0; top: 389px; width: 775px; height: 42px; }
  .footer-web {
    position: absolute; left: 456px; width: 300px; top: 398px;
    text-align: center; font-size: 16px; font-weight: 500; color: var(--ink-dark);
  }
</style>
</head>
<body>
<main class="sheet">

  <section class="card card--back" aria-label="Card back: services">
    <span class="rule" style="left:46px; top:46px; width:37px;"></span>
    <p class="accreditation display">Accredited Guild &amp; Tower KSR Level 3, QTRB</p>
    <span class="rule" style="left:692px; top:46px; width:37px;"></span>

    <p class="services-title"><span class="stars">✷✷✷✷✷✷✷✷✷✷</span>OUR SERVICES<span class="stars">✷✷✷✷✷✷✷✷✷✷</span></p>

    <ul class="service-list service-list--left">
      <li>Emergency Lock Out</li>
      <li>New Lock Fitting &amp;<br>Replacement</li>
      <li>High Security Upgrades</li>
    </ul>

    <div class="brand-mark">
      <span class="brand-mark__name">Brackenfold<br>Latches</span>
    </div>

    <ul class="service-list service-list--right">
      <li>UPVC lock repairs</li>
      <li>Mobile Key Cutting</li>
      <li>Free Security Reviews</li>
    </ul>

    <span class="rule rule--bronze" style="left:46px; top:381px; width:131px;"></span>
    <p class="assurance display">Fully Insured &amp; PVX Checked</p>
    <span class="rule rule--bronze" style="left:598px; top:381px; width:131px;"></span>
  </section>

  <section class="card card--front" aria-label="Card front: contact">
    <div class="tab-block"></div>
    <div class="name-plate">
      <h1 class="name-plate__name">ROB FENWICK</h1>
      <p class="name-plate__role">CEO/OWNER</p>
      <span class="name-plate__line"></span>
    </div>

    <div class="contact contact--phone">
      <span class="contact__icon">
        <svg width="26" height="26" viewBox="0 0 24 24" aria-hidden="true"><path fill="#fff" d="M6.6 10.8a15.1 15.1 0 0 0 6.6 6.6l2.2-2.2a1 1 0 0 1 1-.25 11.4 11.4 0 0 0 3.6.57 1 1 0 0 1 1 1V20a1 1 0 0 1-1 1A17 17 0 0 1 3 4a1 1 0 0 1 1-1h3.5a1 1 0 0 1 1 1c0 1.25.2 2.45.57 3.57a1 1 0 0 1-.25 1z"/></svg>
      </span>
      <p class="contact__text">018 - 2357 - 4419<br>078 - 4159 - 2637</p>
    </div>

    <div class="contact contact--web">
      <span class="contact__icon">
        <svg width="28" height="28" viewBox="0 0 24 24" aria-hidden="true"><circle cx="12" cy="12" r="10" fill="none" stroke="#fff" stroke-width="1.6"/><path fill="none" stroke="#fff" stroke-width="1.4" d="M2 12h20M12 2c3 3 3 17 0 20M12 2c-3 3-3 17 0 20"/></svg>
      </span>
      <p class="contact__text">www.brackenfoldlatches.com<br>contact@brackenfoldlatches.com</p>
    </div>

    <div class="contact contact--place">
      <span class="contact__icon">
        <svg width="24" height="28" viewBox="0 0 24 28" aria-hidden="true"><path fill="#fff" d="M12 1a9 9 0 0 0-9 9c0 6.5 9 17 9 17s9-10.5 9-17a9 9 0 0 0-9-9zm0 12.5A3.5 3.5 0 1 1 12 6.5a3.5 3.5 0 0 1 0 7z"/></svg>
      </span>
      <p class="contact__text">Address line goes here<br>street name, country name</p>
    </div>

    <div class="brand-mark">
      <span class="brand-mark__name">Brackenfold<br>Latches</span>
    </div>
    <p class="trade display">LOCKSMITH</p>

    <svg class="footer-band" viewBox="0 0 775 42" preserveAspectRatio="none" aria-hidden="true">
      <rect x="420" y="0" width="355" height="42" fill="#ffffff" stroke="#999" stroke-width="0.6"/>
      <polygon points="0,0 420,0 462,42 0,42" fill="#7f4614"/>
      <polygon points="408,0 420,0 462,42 450,42" fill="#000"/>
      <polygon points="420,0 430,0 472,42 462,42" fill="#000"/>
    </svg>
    <p class="footer-web">www.brackenfoldlatches.com</p>
  </section>

</main>
</body>
</html>
```